Bramblewick Dill Pickles needs your smart gourmet Design

Looking for a smart design for a dill pickle jar container. The text
Bramblewick Dill Pickles.
Simply Picklelicious.

A tasty reason to raid the refrigerator.

Target Market(s)

Foodies, farmers market types.

Font styles to use
Serif
Sans Serif

Colors

Designer to choose colors to be used in the design.

Requirements
Must have
• Attractive design to entice foodies to buy my Pickles. Not cluttered, easy to read.
Nice to have
• Pickles, garlic. Modern.
Should not have
• Clutter. No script text.

```html
<!DOCTYPE html>
<html lang="en">
<head>
<meta charset="utf-8">
<title>Bramblewick Dill Pickles – Jar Label</title>
<link rel="stylesheet" href="https://fonts.googleapis.com/css2?family=Alfa+Slab+One&family=Cinzel:wght@600&family=Oswald:wght@600&display=swap">
<style>
  :root {
    --page: #f3f3f1;
    --label-white: #ffffff;
    --pickle-green: #364636;
    --orange: #f8a41e;
    --ink: #1c1c1c;
    --steel-dark: #3a3f48;
    --steel-light: #f2f2f2;
    --garlic: #e6dcd8;
    --dill: #5d8b3a;
  }
  * { margin: 0; padding: 0; box-sizing: border-box; }
  html, body { width: 1200px; height: 1200px; overflow: hidden; background: var(--page); }
  .canvas { position: relative; width: 1200px; height: 1200px; }

  .label { position: absolute; left: 0; top: 351px; width: 1200px; height: 498px; background: var(--label-white); overflow: hidden; }

  .side-panel { position: absolute; top: 0; height: 100%; background: var(--pickle-green); }
  .side-panel--left { left: 0; width: 292px; }
  .side-panel--right { left: 880px; width: 320px; }

  .steel-bar {
    position: absolute; top: 0; height: 100%; width: 13px;
    background: linear-gradient(to bottom, var(--steel-dark) 0%, var(--steel-light) 22%, #9a9ea5 40%, var(--steel-light) 55%, #2e3036 78%, var(--steel-light) 92%, #6c7078 100%);
  }
  .steel-bar--left { left: 298px; }
  .steel-bar--right { left: 857px; }

  .orange-block { position: absolute; background: var(--orange); }
  .orange-block--top { left: 326px; top: 0; width: 117px; height: 148px; }
  .orange-block--bottom { left: 322px; top: 244px; width: 120px; height: 254px; }

  .brand {
    position: absolute; left: 640px; top: 30px; width: 200px;
    display: flex; flex-direction: column; align-items: center; gap: 6px;
    color: var(--ink); font-family: "Oswald", sans-serif; font-weight: 600;
  }
  .brand__est, .brand__place { font-size: 10px; letter-spacing: 1.5px; }
  .brand__row { display: flex; align-items: center; gap: 10px; }
  .brand__name { font-size: 38px; line-height: 1; letter-spacing: 1px; }
  .brand__dot { width: 22px; height: 22px; border-radius: 50%; background: var(--dill); }

  .headline {
    position: absolute; left: 322px; top: 166px; width: 528px;
    font-family: "Alfa Slab One", serif; font-size: 50px; line-height: 1;
    color: var(--ink); letter-spacing: 0; white-space: nowrap; text-align: center;
    text-shadow: 2px 2px 0 #ffffff, 4px 4px 0 var(--ink);
  }

  .variety-pill {
    position: absolute; left: 464px; top: 246px; width: 368px; height: 62px;
    background: var(--ink); border-radius: 18px;
    display: flex; align-items: center; justify-content: center;
  }
  .variety-pill::before {
    content: ""; position: absolute; inset: 4px;
    border: 2px solid var(--label-white); border-radius: 14px;
  }
  .variety-pill__text {
    font-family: "Cinzel", serif; font-weight: 600; font-size: 40px; line-height: 1;
    color: var(--label-white); letter-spacing: 1px;
  }

  .ingredient-art {
    position: absolute; left: 352px; top: 342px; width: 326px; height: 152px;
    border-radius: 40px 60px 20px 30px;
    background: radial-gradient(ellipse at 30% 60%, var(--garlic) 0%, #efe6d2 40%, rgba(93,139,58,0.55) 75%, rgba(255,255,255,0) 100%);
  }
</style>
</head>
<body>
<main class="canvas">
  <section class="label">
    <div class="side-panel side-panel--left"></div>
    <div class="side-panel side-panel--right"></div>
    <div class="steel-bar steel-bar--left"></div>
    <div class="steel-bar steel-bar--right"></div>

    <div class="orange-block orange-block--top"></div>
    <div class="orange-block orange-block--bottom"></div>

    <div class="brand">
      <span class="brand__est">EST 1995</span>
      <div class="brand__row">
        <span class="brand__name">Brinewell</span>
        <span class="brand__dot"></span>
      </div>
      <span class="brand__place">MARLOW CREEK</span>
    </div>

    <h1 class="headline">BRAMBLEWICK</h1>

    <div class="variety-pill"><span class="variety-pill__text">Dill Pickles</span></div>

    <div class="ingredient-art" role="img" aria-label="Illustration of garlic bulbs, peeled cloves and a sprig of fresh dill"></div>
  </section>
</main>
</body>
</html>
```